VELMIT Business Card

VELMIT (www.velmitpools.example) is a veteran in the swimming pool maintenance and repair business..we have served our clients for 15 years and have a research chemist, an electrician, a plumber and a pool building contractor (in part) on staff...We want to provide a business card that has a dual purpose, that people want to keep around, that leaves people speechless in the sense that they understand the mission of and the experience level of the TEAM at VELMIT.

Target Market(s)

persons who enjoy swimming and make it a priority to swim

Industry/Entity Type

Building

Font styles to use
Serif
Sans Serif

Colors
85acd3
3176b5
95b6d8
3276b5
0355a3
0555a3
0255a3
0455a3
85abd2

Requirements
Must have
• name, title, address, email, text
Nice to have
• a die cut shape
Should not have
• cartoons, pictures of pools

```html
<!DOCTYPE html>
<html lang="en">
<head>
<meta charset="utf-8">
<title>VELMIT Business Card</title>
<link href="https://fonts.googleapis.com/css2?family=Josefin+Sans:wght@300;400;600&family=Poiret+One&display=swap" rel="stylesheet">
<style>
  :root {
    --bg: #ebe7e1;
    --navy: #0555a3;
    --brand: #3a93b8;
    --sky: #4bb3e0;
    --white: #ffffff;
    --ink: #1a1a1a;
  }
  * { margin: 0; padding: 0; box-sizing: border-box; }
  html, body { width: 1200px; height: 1000px; overflow: hidden; }
  body {
    background: var(--bg);
    position: relative;
    font-family: "Josefin Sans", sans-serif;
  }
  .card {
    position: absolute;
    border-radius: 24px 100px 24px 100px;
    overflow: hidden;
    box-shadow: 0 6px 14px rgba(0,0,0,0.18);
  }
  .card-front {
    left: 40px; top: 60px; width: 720px; height: 420px;
    background: var(--navy);
    color: var(--white);
  }
  .card-back {
    left: 470px; top: 530px; width: 700px; height: 420px;
    background: var(--white);
  }
  .brand-corner {
    position: absolute; right: 36px; top: 50px;
    text-align: center;
  }
  .brand-corner .brand-name {
    font-size: 44px; font-weight: 400; color: var(--brand);
    letter-spacing: 2px;
  }
  .brand-corner .tagline {
    font-size: 15px; color: var(--brand); letter-spacing: 1.5px;
    margin-top: 4px;
  }
  .person { position: absolute; left: 56px; top: 180px; }
  .person .name {
    font-size: 34px; font-weight: 600; color: var(--ink);
    padding-bottom: 4px; border-bottom: 2px solid var(--white);
    padding-right: 4px;
  }
  .person .role {
    font-family: "Poiret One", sans-serif;
    font-size: 28px; margin-top: 6px; color: var(--white);
  }
  .contacts {
    position: absolute; left: 385px; top: 290px;
    list-style: none;
    font-family: "Poiret One", sans-serif;
    font-size: 21px; line-height: 29px; font-weight: 400;
  }
  .contacts li { display: flex; align-items: center; gap: 8px; }
  .contacts svg { width: 20px; height: 20px; fill: var(--ink); flex: none; }
  .brand-center {
    position: absolute; left: 0; right: 0; top: 130px; text-align: center;
  }
  .brand-center .brand-name {
    font-size: 92px; font-weight: 600; color: var(--brand); letter-spacing: 4px;
    padding-left: 20px;
  }
  .brand-center .tagline {
    font-size: 26px; font-weight: 400; color: var(--sky); letter-spacing: 2px;
    margin-top: 4px;
  }
  .wave-band { position: absolute; left: 0; bottom: 0; width: 700px; height: 110px; }
</style>
</head>
<body>
  <section class="card card-front">
    <div class="brand-corner">
      <div class="brand-name">VELMIT</div>
      <div class="tagline">CLEAR WATER...ELEVATED</div>
    </div>
    <div class="person">
      <div class="name">Your Name</div>
      <div class="role">Manager</div>
    </div>
    <ul class="contacts">
      <li><svg viewBox="0 0 20 20"><circle cx="10" cy="10" r="9" fill="none" stroke="#1a1a1a" stroke-width="1.6"/><path d="M6.5 5.5l2 0 1 2.5-1.3 1a6 6 0 0 0 2.8 2.8l1-1.3 2.5 1v2c-4.5 0.4-8.4-3.5-8-8z"/></svg>your phone number</li>
      <li><svg viewBox="0 0 20 20"><rect x="2" y="5" width="16" height="11"/><path d="M2 5l8 6 8-6" fill="none" stroke="#0555a3" stroke-width="1.4"/></svg>your email@mailhost.example</li>
      <li><svg viewBox="0 0 20 20"><path d="M10 2l9 8h-3v8h-4v-5H8v5H4v-8H1z"/></svg>your address stret</li>
    </ul>
  </section>

  <section class="card card-back">
    <div class="brand-center">
      <div class="brand-name">VELMIT</div>
      <div class="tagline">CLEAR WATER...ELEVATED</div>
    </div>
    <svg class="wave-band" viewBox="0 0 700 110" preserveAspectRatio="none">
      <path fill="#0555a3" d="M0 12
        Q35 50 70 12 Q105 50 140 12 Q175 50 210 12 Q245 50 280 12
        Q315 50 350 12 Q385 50 420 12 Q455 50 490 12 Q525 50 560 12
        Q595 50 630 12 Q665 50 700 12 L700 110 L0 110 Z"/>
    </svg>
  </section>
</body>
</html>
```